Alder Court Parking Lot Flyer

I need a 1/2 page flyer to look and feel like my website. With all the relevant information like phone # and map to our office. It needs to look and feel like a shortened or brief version of our website but on paper. I would like the colors to be the same palette as the website and I would like the flyer to be full color front and back. The web address is pinonridgelegalteam.com
Our logo is on the website and all relevant information can be viewed there as well. Please include our web address on the flyer as well.
This is for a Law Firm so it needs to be very PROFESSIONAL Looking.
DO NOT USE OUR PHOTOGRAPHS OR PICTURES OF US.

Target Market(s)

People visiting the courthouse who need to hire a criminal defense attorney immediately.

Industry/Entity Type

Court

Font styles to use
Serif

Colors

Designer to choose colors to be used in the design.

Requirements
Must have
• Contact information and map. Web address is crucial as well.

```html
<!DOCTYPE html>
<html lang="en">
<head>
<meta charset="utf-8">
<title>Pinon Ridge Legal Team – Parking Lot Flyer</title>
<link rel="stylesheet" href="https://fonts.googleapis.com/css2?family=Cinzel:wght@400;700&family=Crimson+Text:wght@400&family=Open+Sans:wght@700&display=swap">
<style>
  :root {
    --teal: #27c3d6;
    --teal-deep: #1e7f86;
    --charcoal: #2f2f31;
    --ink: #1f1f1f;
    --paper: #e8e9ea;
    --paper-light: #f4f5f5;
    --white: #ffffff;
    --backdrop: #1d1d1d;
    --map-dark: #232323;
    --map-gold: #a08a5c;
  }
  * { margin: 0; padding: 0; box-sizing: border-box; }
  html, body { width: 1200px; height: 907px; overflow: hidden; background: var(--backdrop); }
  .flyer {
    position: absolute; left: 78px; top: 108px; width: 1040px; height: 692px;
    background: linear-gradient(180deg, var(--paper-light), var(--paper));
    overflow: hidden;
  }
  .shapes { position: absolute; inset: 0; }
  .intro {
    position: absolute; left: 30px; top: 52px; width: 318px;
    font: 17px/24.5px "Crimson Text", Georgia, serif; color: var(--ink);
    text-align: justify;
  }
  .brand {
    position: absolute; left: 415px; top: 28px; display: flex; align-items: center; gap: 24px;
  }
  .brand-mark { width: 80px; height: 80px; border: 3px solid var(--white); border-radius: 50%; }
  .brand-name {
    font: 400 30px/38px "Cinzel", Georgia, serif; color: var(--white); letter-spacing: 1px;
  }
  .services { position: absolute; top: 168px; left: 380px; width: 640px; height: 140px; }
  .service { position: absolute; top: 0; width: 200px; text-align: center; }
  .service svg { display: block; margin: 0 auto; }
  .service-label {
    margin-top: 12px; font: 700 19px/1 "Open Sans", Arial, sans-serif; color: var(--ink);
  }
  .tagline-band {
    position: absolute; left: 0; top: 328px; width: 1040px; height: 58px;
    background: var(--charcoal);
    font: 400 38px/58px "Cinzel", Georgia, serif; color: var(--white);
    text-align: center; letter-spacing: 1.5px;
  }
  .headline { position: absolute; left: 36px; top: 430px; }
  .headline-lead { font: 400 50px/1 "Cinzel", Georgia, serif; color: var(--ink); letter-spacing: 2px; }
  .headline-focus { margin-top: 22px; font: 700 62px/1 "Cinzel", Georgia, serif; color: var(--teal-deep); letter-spacing: 4px; }
  .office-map {
    position: absolute; left: 770px; top: 400px; width: 224px; height: 224px; border-radius: 50%;
    border: 7px solid var(--teal);
    background: radial-gradient(circle at 50% 45%, var(--map-gold) 0 14%, var(--map-dark) 15% 100%);
  }
  .web-address {
    position: absolute; left: 36px; top: 620px;
    font: 400 22px/46px "Cinzel", Georgia, serif; color: var(--ink); letter-spacing: 1px;
  }
  .phone {
    position: absolute; left: 672px; top: 638px; display: flex; align-items: center; gap: 28px;
    font: 400 38px/54px "Cinzel", Georgia, serif; color: var(--white);
  }
</style>
</head>
<body>
<main class="flyer">
  <svg class="shapes" width="1040" height="692" viewBox="0 0 1040 692" aria-hidden="true">
    <rect x="0" y="0" width="1040" height="24" fill="var(--teal)"/>
    <path d="M390 0 H1040 V140 H460 Q420 140 410 110 L395 40 Q390 24 390 0 Z" fill="var(--teal)"/>
    <path d="M0 24 H368 Q390 24 390 46 V326 H0 Z" fill="var(--white)" opacity="0.85"/>
    <path d="M0 620 H525 Q548 620 548 642 Q548 665 525 665 H0 Z" fill="var(--teal)"/>
    <path d="M560 692 Q600 637 660 637 H1040 V692 Z" fill="var(--charcoal)"/>
  </svg>

  <p class="intro">Have you recently been arrested for an alleged criminal offense? If so, you understand how complex the criminal court system can be in New Mexico as well as the number of different forms you must fill out even before a court date is set. An experienced criminal law attorney can help ensure that everything gets filed appropriately and can prepare you for a hearing.</p>

  <div class="brand">
    <span class="brand-mark"></span>
    <span class="brand-name">Pinon Ridge<br>Legal Team</span>
  </div>

  <div class="services">
    <div class="service" style="left:2px">
      <svg width="90" height="90" viewBox="0 0 90 90" aria-hidden="true">
        <circle cx="45" cy="45" r="42" fill="var(--charcoal)" stroke="var(--teal)" stroke-width="6"/>
        <path d="M31 28 H59 V38 Q59 52 45 54 Q31 52 31 38 Z" fill="var(--white)"/>
        <path d="M31 32 H24 Q24 44 33 46 M59 32 H66 Q66 44 57 46" stroke="var(--white)" stroke-width="3" fill="none"/>
        <rect x="42" y="53" width="6" height="8" fill="var(--white)"/>
        <rect x="34" y="61" width="22" height="5" rx="1" fill="var(--white)"/>
      </svg>
      <p class="service-label">Free Consultation</p>
    </div>
    <div class="service" style="left:255px">
      <svg width="90" height="90" viewBox="0 0 90 90" aria-hidden="true">
        <circle cx="45" cy="45" r="42" fill="var(--charcoal)" stroke="var(--teal)" stroke-width="6"/>
        <path d="M38 33 V28 H52 V33" stroke="var(--white)" stroke-width="3" fill="none"/>
        <rect x="26" y="33" width="38" height="28" rx="4" fill="var(--white)"/>
        <rect x="26" y="44" width="38" height="2" fill="var(--charcoal)"/>
      </svg>
      <p class="service-label">Meet the Attorneys</p>
    </div>
    <div class="service" style="left:452px">
      <svg width="90" height="90" viewBox="0 0 90 90" aria-hidden="true">
        <circle cx="45" cy="45" r="42" fill="var(--charcoal)" stroke="var(--teal)" stroke-width="6"/>
        <path d="M45 25 A20 18 0 1 1 35 59 L26 64 L30 55 A20 18 0 0 1 45 25 Z" fill="var(--white)"/>
        <circle cx="37" cy="43" r="2.5" fill="var(--teal)"/>
        <circle cx="45" cy="43" r="2.5" fill="var(--teal)"/>
        <circle cx="53" cy="43" r="2.5" fill="var(--teal)"/>
      </svg>
      <p class="service-label">Case result</p>
    </div>
  </div>

  <h2 class="tagline-band">Albuquerque Criminal Defense Law Firm</h2>

  <h1 class="headline">
    <span class="headline-lead">Clearing your name is</span>
    <span class="headline-focus" style="display:block">OUR #1 PRIORITY</span>
  </h1>

  <div class="office-map" role="img" aria-label="Street map showing the office location near the courthouse"></div>

  <p class="web-address">WWW.PINONRIDGELEGALTEAM.COM</p>

  <p class="phone">
    <svg width="34" height="34" viewBox="0 0 34 34" aria-hidden="true">
      <circle cx="17" cy="17" r="16" fill="var(--teal)"/>
      <path d="M12 9 L15 9 L16 14 L14 15.5 Q16 20 19 21 L20.5 19 L25 20 L25 23 Q24 26 21 25.5 Q11 22 9 12.5 Q9 9.5 12 9 Z" fill="var(--charcoal)"/>
    </svg>
    505.555.0147
  </p>
</main>
</body>
</html>
```